Fitness Clothing Apparel Business Card

This project is linked to Fitness Clothing Apparel, KESTRO, Looking for AWESOME Logo Design!!!.

Our company needs a Business Card Design. Please refer to our original project in the link above.

Hi, I'm looking for a professional logo design which will help brand my clothing and nutrition supplement company. The winner of this contest may be hired again in the future to help design some flyers, banners, graphics, etc.

A little background about the company...
KESTRO Fitness is a new fitness clothing and nutrition company based in Southern California... near the mecca of bodybuilding, Harlow Cove! Our company is based around the culture of fitness and bodybuilding. We design clothing that are functional yet appealing for an athletic individual.

What I would like to see on business card...
The card has communicate our brand values. It needs to have attitude yet professionally done. Our brand colors are black, red, and white.

Target Market(s)

Fitness and bodybuilding enthusiasts

Industry/Entity Type

Nutrition

Font styles to use
Serif
Sans Serif
Decorative
Script

Colors

Designer to choose colors to be used in the design.

Requirements
Must have
• our company logo
Nice to have
• red and black, an abstract design of a bull
Should not have
• I'm open to all ideas, appearance is important

```html
<!DOCTYPE html>
<html lang="en">
<head>
<meta charset="utf-8">
<title>KESTRO Business Card</title>
<link rel="stylesheet" href="https://fonts.googleapis.com/css2?family=Michroma&family=Questrial&display=swap">
<style>
  :root {
    --ink: #000000;
    --paper: #ffffff;
    --canvas: #ffffff;
    --rule: #1a1a1a;
    --art-light-a: #ffffff;
    --art-light-b: #d9d9d9;
    --art-dark-a: #000000;
    --art-dark-b: #3a3a3a;
  }
  * { box-sizing: border-box; margin: 0; padding: 0; }
  html, body {
    width: 1200px;
    height: 1200px;
    overflow: hidden;
    background: var(--canvas);
  }
  .canvas {
    position: relative;
    width: 1200px;
    height: 1200px;
    background: var(--canvas);
  }
  .card {
    position: absolute;
    width: 601px;
    height: 346px;
    overflow: hidden;
  }
  .card--front {
    left: 310px;
    top: 216px;
    background: var(--ink);
  }
  .card--back {
    left: 299px;
    top: 647px;
    background: var(--paper);
    border: 1.5px solid var(--rule);
  }
  .bull-art {
    position: absolute;
    left: 0;
    border-radius: 0 45% 8% 0 / 0 55% 10% 0;
  }
  .card--front .bull-art {
    top: 10px;
    width: 302px;
    height: 336px;
    background: linear-gradient(160deg, var(--art-light-a) 0%, var(--art-light-b) 100%);
  }
  .card--back .bull-art {
    top: 15px;
    width: 300px;
    height: 331px;
    background: linear-gradient(160deg, var(--art-dark-a) 0%, var(--art-dark-b) 100%);
  }
  .brand--front {
    position: absolute;
    left: 311px;
    top: 268px;
    font-family: "Michroma", sans-serif;
    font-weight: 400;
    font-size: 27px;
    line-height: 36px;
    letter-spacing: 10px;
    color: var(--paper);
    white-space: nowrap;
  }
  .contact {
    position: absolute;
    right: 40px;
    top: 74px;
    text-align: right;
    color: var(--ink);
  }
  .contact-name {
    font-family: "Michroma", sans-serif;
    font-size: 25px;
    letter-spacing: 2px;
    line-height: 1;
    margin-bottom: 22px;
  }
  .contact-lines {
    font-family: "Questrial", sans-serif;
    font-size: 21px;
    line-height: 28px;
  }
  .contact-lines + .contact-lines {
    margin-top: 29px;
  }
</style>
</head>
<body>
<main class="canvas">
  <section class="card card--front" aria-label="Business card front">
    <div class="bull-art" role="img" aria-label="Abstract white bull illustration"></div>
    <p class="brand--front">KESTRO</p>
  </section>

  <section class="card card--back" aria-label="Business card back">
    <div class="bull-art" role="img" aria-label="Abstract black bull illustration"></div>
    <div class="contact">
      <p class="contact-name">JOHN DOE</p>
      <p class="contact-lines">333 address<br>city, state, 55555</p>
      <p class="contact-lines">555.555.5555<br>JDoe@website.com<br>www.website.com</p>
    </div>
  </section>
</main>
</body>
</html>
```